Redesign Company Website WRAPTIDE

We want to redesign the web page of the company using some actual pictures such as the ones that show the production line, equipment and the plant. About the products picture i am ok if upgrade for new ones o keep some of them.
PLease visiti: www.lumodiseno.example.ve/wraptide/ to check the actual page.

Target Market(s)

Processors and Producers of:
Cheese, Fresh Meat, Sausages, Poultry, Processed Meats,

Coding

Coded - Design and coding required

Number of Pages Required

5+ page

Requirements
Must have
• Bilingual Spanish/English
Nice to have

Should not have
• Blogs, or any customer interaction, no particular brand must be shown, must be all generic.

```html
<!DOCTYPE html>
<html lang="en">
<head>
<meta charset="utf-8">
<title>WRAPTIDE – Flexible Packaging Solutions</title>
<link href="https://fonts.googleapis.com/css2?family=Poppins:ital,wght@0,400;0,500;0,600;0,700;1,700;1,800&family=Roboto:wght@300;400;700&display=swap" rel="stylesheet">
<style>
:root{
  --teal:#0aa19a;
  --teal-dark:#17a9a0;
  --lime:#c8e03a;
  --green:#5cc246;
  --green-mid:#8fd23c;
  --yellow:#dfe34a;
  --orange:#ff6a00;
  --ink:#1a1a1a;
  --body:#3a3a3a;
  --footer:#073a36;
  --white:#ffffff;
}
*{margin:0;padding:0;box-sizing:border-box}
html,body{width:682px;height:1200px;overflow:hidden;background:var(--white)}
body{position:relative;font-family:"Roboto",sans-serif;color:var(--body)}
.abs{position:absolute}

.topbar{left:0;top:0;width:682px;height:20px;background:var(--teal);color:var(--white);font-family:"Poppins",sans-serif;font-size:5.5px;font-weight:600}
.topbar .lang{position:absolute;left:100px;top:6px;display:flex;align-items:center;gap:3px}
.topbar .lang i{display:inline-block;width:7px;height:5px;background:#2a4aa0;border:1px solid #d22}
.topbar .tagline{position:absolute;right:98px;top:6px;letter-spacing:.1px}

.hero{left:0;top:20px;width:682px;height:313px;background:linear-gradient(100deg,var(--green) 0%,var(--green-mid) 55%,var(--yellow) 100%)}
.logo{position:absolute;left:98px;top:10px;font-family:"Poppins",sans-serif;font-weight:700;font-size:17px;color:var(--white);letter-spacing:1px}
.nav{position:absolute;right:98px;top:14px;display:flex;gap:10px;font-family:"Poppins",sans-serif;font-weight:600;font-size:5.5px;color:var(--ink)}
.hero-product{position:absolute;left:105px;top:64px;width:232px;height:209px;border-radius:4px;background:linear-gradient(90deg,#2ec4b6 0%,#e8e8e8 15%,#c9b800 30%,#c9b800 68%,#a12a12 80%,#ececec 100%)}
.hero-leaves{position:absolute;right:0;top:20px;width:54px;height:220px;border-radius:30px 0 0 30px;background:linear-gradient(180deg,#4c6b1e,#2e4a14)}
.hero h1{position:absolute;left:365px;top:88px;font-family:"Poppins",sans-serif;font-style:italic;font-weight:800;font-size:30px;line-height:30px;color:var(--white)}
.hero .sub{position:absolute;left:366px;top:185px;font-family:"Poppins",sans-serif;font-style:italic;font-weight:700;font-size:8px;color:var(--ink)}
.btn{position:absolute;left:366px;top:209px;width:79px;height:22px;background:var(--orange);color:var(--white);font-family:"Poppins",sans-serif;font-weight:600;font-size:8px;letter-spacing:.6px;display:flex;align-items:center;justify-content:center}

.packaging{left:0;top:333px;width:682px;height:182px;background:linear-gradient(100deg,var(--green) 0%,var(--green-mid) 60%,#b9dc45 100%)}
.packaging h2{position:absolute;left:0;width:682px;top:6px;text-align:center;font-family:"Poppins",sans-serif;font-weight:600;font-size:20px;color:var(--white)}
.pack{position:absolute;top:49px;width:120px;text-align:center}
.pack svg{display:block;margin:0 auto}
.pack span{display:block;margin-top:9px;font-family:"Poppins",sans-serif;font-weight:500;font-size:9px;letter-spacing:1px;color:var(--ink)}
.arrow{position:absolute;top:83px}

.welcome{left:0;top:515px;width:682px;height:347px;background:var(--white)}
.welcome h2{position:absolute;left:98px;top:80px;font-family:"Poppins",sans-serif;font-style:italic;font-weight:800;font-size:30px;line-height:32px;color:var(--teal-dark)}
.welcome p{position:absolute;left:98px;width:266px;font-size:7.4px;line-height:10.1px;font-weight:300;color:var(--body)}
.welcome .p1{top:155px}
.welcome .p2{top:246px}
.welcome-photo{position:absolute;left:375px;top:82px;width:230px;height:206px;border-radius:40px 60px 30px 70px;background:radial-gradient(circle at 60% 40%,#f2d6dc,#e9c3cb 50%,#f1ece0 100%)}
.tri{position:absolute}

.testimonial{left:0;top:862px;width:682px;height:187px;background:linear-gradient(100deg,var(--yellow) 0%,#bddd3e 50%,var(--green-mid) 100%);text-align:center}
.testimonial h3{position:absolute;top:37px;width:682px;font-family:"Poppins",sans-serif;font-weight:500;font-size:15px;color:var(--white)}
.stars{position:absolute;top:58px;left:0;width:682px;display:flex;justify-content:center;gap:1px}
.testimonial blockquote{position:absolute;top:75px;left:130px;width:422px;font-family:"Roboto",sans-serif;font-weight:700;font-size:13.5px;line-height:16.5px;color:var(--white)}
.testimonial .name{position:absolute;top:118px;width:682px;font-weight:700;font-size:8.5px;color:var(--white)}
.dots{position:absolute;top:137px;left:0;width:682px;display:flex;justify-content:center;gap:3px}
.dots i{width:4.5px;height:4.5px;border-radius:50%;background:#1a1a1a}
.dots i.on{background:var(--white)}
.test-leaves{position:absolute;left:4px;bottom:0;width:246px;height:52px;border-radius:40px 40px 0 0;background:linear-gradient(90deg,#2f4715,#4d6b20)}

.footer{left:0;top:1049px;width:682px;height:121px;background:var(--footer);color:var(--white)}
.fcol{position:absolute;top:31px}
.fcol h4{font-family:"Poppins",sans-serif;font-weight:600;font-size:10px;margin-bottom:10px}
.fcol p,.fcol li{font-size:6.6px;line-height:11.7px;font-weight:400;list-style:none}
.fcol.about p{line-height:9.2px;width:190px}
.social{display:flex;gap:3px}
.social i{width:15px;height:15px;border-radius:50%;background:var(--green-mid)}
.social i:nth-child(2){background:var(--teal)}
.social i:nth-child(3){background:var(--teal-dark)}
.copy{left:0;top:1170px;width:682px;height:30px;background:var(--footer);border-top:1px solid #145048;color:var(--white);font-size:8px;text-align:center;padding-top:9px}
</style>
</head>
<body>

<div class="abs topbar">
  <div class="lang"><i></i>English ▾</div>
  <div class="tagline">SOMOS UNA EMPRESA CONVERTIDORA DEEMPAQUES FLEXIBLES</div>
</div>

<header class="abs hero">
  <div class="logo">WRAPTIDE</div>
  <nav class="nav"><span>NOSOTROS</span><span>MERCADOS</span><span>EMPAQUES</span><span>INTERES</span><span>CONTACTO</span></nav>
  <div class="hero-product" role="img" aria-label="Stand-up pouches in teal, white, yellow and red with vacuum-packed sausages and film rolls"></div>
  <div class="hero-leaves" role="img" aria-label="Tropical leaves at the page edge"></div>
  <h1>FLEXIBLE<br>PACKAGING<br>SOLUTIONS</h1>
  <div class="sub">Help our clients to be the consumer's preference.</div>
  <div class="btn">LEARN MORE</div>
</header>

<section class="abs packaging">
  <h2>Our Packaging</h2>
  <div class="pack" style="left:106px">
    <svg width="76" height="76" viewBox="0 0 76 76"><circle cx="38" cy="38" r="36" fill="none" stroke="#fff" stroke-width="1.4" stroke-dasharray="1.5 2"/><circle cx="38" cy="38" r="32" fill="#c8e03a"/><path d="M28 28h6v4h8v-4h6v22H28z" fill="none" stroke="#fff" stroke-width="2.2" stroke-linejoin="round"/></svg>
    <span>SELF-STANDING BAGS</span>
  </div>
  <svg class="arrow" style="left:234px" width="28" height="10" viewBox="0 0 28 10"><path d="M1 2q12 9 25 2" fill="none" stroke="#111" stroke-width="1.2"/><path d="M22 1l4 3-4 2" fill="none" stroke="#111" stroke-width="1.2"/></svg>
  <div class="pack" style="left:262px;width:150px">
    <svg width="76" height="76" viewBox="0 0 76 76"><circle cx="38" cy="38" r="36" fill="none" stroke="#fff" stroke-width="1.4" stroke-dasharray="1.5 2"/><circle cx="38" cy="38" r="32" fill="#c8e03a"/><rect x="28" y="22" width="20" height="30" fill="none" stroke="#fff" stroke-width="2"/><line x1="28" y1="28" x2="48" y2="28" stroke="#fff" stroke-width="1.4"/><circle cx="38" cy="40" r="5" fill="none" stroke="#fff" stroke-width="1.6"/></svg>
    <span>HEAT SHRINKABLE BAGS</span>
  </div>
  <svg class="arrow" style="left:412px" width="28" height="10" viewBox="0 0 28 10"><path d="M1 8q12-9 25-4" fill="none" stroke="#111" stroke-width="1.2"/><path d="M22 2l4 2-4 3" fill="none" stroke="#111" stroke-width="1.2"/></svg>
  <div class="pack" style="left:454px">
    <svg width="76" height="76" viewBox="0 0 76 76"><circle cx="38" cy="38" r="36" fill="none" stroke="#fff" stroke-width="1.4" stroke-dasharray="1.5 2"/><circle cx="38" cy="38" r="32" fill="#0aa19a"/><rect x="29" y="21" width="18" height="33" fill="none" stroke="#fff" stroke-width="2"/><rect x="32" y="27" width="12" height="21" fill="none" stroke="#fff" stroke-width="1.2"/><ellipse cx="38" cy="37" rx="3.5" ry="2.5" fill="none" stroke="#fff" stroke-width="1.2"/></svg>
    <span>VACCUM BAGS</span>
  </div>
</section>

<section class="abs welcome">
  <svg class="tri" style="left:234px;top:46px" width="22" height="22" viewBox="0 0 22 22"><path d="M0 0L22 8L10 22z" fill="#8ccf45" opacity=".85"/></svg>
  <svg class="tri" style="left:382px;top:34px" width="34" height="38" viewBox="0 0 34 38"><path d="M0 0H34L14 38z" fill="#7cc23f"/></svg>
  <svg class="tri" style="left:108px;top:262px" width="24" height="34" viewBox="0 0 24 34"><path d="M0 10L24 0L8 34z" fill="#a5d66a"/></svg>
  <svg class="tri" style="left:518px;top:290px" width="26" height="30" viewBox="0 0 26 30"><path d="M10 0L26 16L0 30z" fill="#a5d66a"/></svg>
  <h2>WELCOME TO<br>WRAPTIDE</h2>
  <p class="p1">Somos una empresa convertidora de empaques flexibles establecida en Maracaibo, Venezuela. Contamos con 30 años de experiencia en el mercado de empaques flexibles. Nacimos a partir de la necesidad de nuestra empresa Matriz Quimiterra, de crear una empresa enfocada solo en el sector empaques para darle así el impulso a esta unidad de negocios el cual ha experimentado un crecimiento sostenido. Mantenemos alianzas estratégicas con Polarfilm (USA) y Northbend Films (Canada) lo que nos permite estar actualizado con las tendencias mundiales en empaques.</p>
  <p class="p2">Estamos en constante actualización tecnológica con nuevos equipos para ofrecer a nuestros clientes empaques de excelente calidad de impresión y formas novedosas.</p>
  <div class="welcome-photo" role="img" aria-label="Vacuum-packed whole chickens and a round white cheese"></div>
</section>

<section class="abs testimonial">
  <div class="test-leaves" role="img" aria-label="Tropical leaves along the bottom edge"></div>
  <h3>WHAT OUR CUSTOMER SAYS</h3>
  <div class="stars">
    <svg width="46" height="9" viewBox="0 0 50 10" fill="#fff"><path id="s" d="M5 0l1.2 3.4H10L7 5.6 8.1 9 5 7 1.9 9 3 5.6 0 3.4h3.8z"/><use href="#s" x="10"/><use href="#s" x="20"/><use href="#s" x="30"/><use href="#s" x="40"/></svg>
  </div>
  <blockquote>Lorem ipsum dolor sit amet, consectetuer adipiscing elit, sed diam nonummy nibh euismod tincidunt ut laoreet.</blockquote>
  <div class="name">JHON DOE</div>
  <div class="dots"><i class="on"></i><i></i><i></i><i></i></div>
</section>

<footer class="abs footer">
  <div class="fcol about" style="left:97px">
    <h4>About Us</h4>
    <p>Maracaibo, Venezuela. Contamos con 30 años de experiencia en el mercado de empaques flexibles. Nacimos a partir de la necesidad de nuestra empresa Matriz Quimiterra, de crear una empresa enfocada solo en el sector empaques para darle así el impulso a esta unidad .</p>
  </div>
  <div class="fcol" style="left:313px">
    <h4>Quick Links</h4>
    <ul><li>Nosotros</li><li>Mercados</li><li>Empaques</li><li>Interes</li><li>Contacto</li></ul>
  </div>
  <div class="fcol" style="left:400px">
    <h4>Contact</h4>
    <p>150th Street with 48th Avenue<br>Maracaibo Industrial Zone<br>ventas@quimiterra.example<br>+58 261-555-0147</p>
  </div>
  <div class="fcol" style="left:525px">
    <h4>Follow Us</h4>
    <div class="social"><i></i><i></i><i></i></div>
  </div>
</footer>
<div class="abs copy">© 2020 wraptide All Rights Reserved.</div>

</body>
</html>
```